New Tech Support Service needs a website design

We need a web design for a new product we are developing that provides tech support to consumers for a small ongoing monthly fee. We are looking for a fresh, technology look and feel. We want the site to have a tech feel - yet not intimidating. Simple and welcoming. We are in need of an initial landing page, sign on page, and a product home page.

Thank you to everyone who submitted designs. It was a very difficult decision!

Industry/Entity Type

Tech

```html
<!DOCTYPE html>
<html lang="en">
<head>
<meta charset="utf-8">
<title>Tech Support Service</title>
<link href="https://fonts.googleapis.com/css2?family=Open+Sans:wght@400;600&family=Hind:wght@300;400&display=swap" rel="stylesheet">
<style>
  :root {
    --blue: #0a6fe0;
    --blue-dark: #0456c4;
    --ink: #2a2a2a;
    --muted: #666a70;
    --rule: #dcdcdc;
    --hero-a: #0d1a2a;
    --hero-b: #24405e;
    --band: #e6e7e9;
    --footer: #2b2b2b;
    --white: #ffffff;
    --wine: #7a1f2b;
    --sq-1: #3b5998;
    --sq-2: #2aa4df;
    --sq-3: #f26b1d;
    --sq-4: #d9262b;
  }
  * { margin: 0; padding: 0; box-sizing: border-box; }
  html, body { width: 680px; height: 1200px; overflow: hidden; background: var(--white); }
  body { position: relative; font-family: "Hind", Arial, sans-serif; color: var(--ink); }

  .site-header { position: absolute; left: 0; top: 0; width: 680px; height: 84px; background: var(--white); }
  .brand { position: absolute; left: 47px; top: 32px; font-weight: 400; font-size: 35px; line-height: 1; color: var(--blue); }
  .main-nav { position: absolute; right: 32px; top: 51px; display: flex; gap: 28px; font-size: 11.5px; color: #333; }

  .hero { position: absolute; left: 0; top: 84px; width: 680px; height: 273px;
    background: radial-gradient(ellipse at 80% 45%, #37506d 0%, transparent 55%), linear-gradient(100deg, var(--hero-b) 0%, var(--hero-a) 55%, #111a24 100%); }
  .hero-title { position: absolute; left: 64px; top: 96px; font-weight: 400; font-size: 23px; line-height: 1.2; color: var(--white); }
  .hero-text { position: absolute; left: 64px; top: 134px; width: 225px; font-size: 10.5px; line-height: 16px; color: var(--white); }
  .hero-btn { position: absolute; left: 64px; top: 176px; width: 63px; height: 20px; background: var(--white); border-radius: 2px; font-size: 10px; line-height: 21px; text-align: center; color: var(--wine); }

  .feature { position: absolute; top: 398px; width: 200px; text-align: center; }
  .feature svg { display: block; margin: 0 auto; }
  .feature h3 { font-weight: 400; font-size: 16px; line-height: 1.2; color: var(--blue); margin-top: 14px; }
  .feature p { font-size: 9.5px; line-height: 14.5px; color: var(--muted); margin-top: 5px; }

  .divider { position: absolute; left: 49px; top: 595px; width: 582px; height: 1px; background: var(--rule); }

  .product-shot { position: absolute; left: 98px; top: 651px; width: 238px; height: 176px; background: linear-gradient(180deg, #f4f5f5 0%, #8a8f86 40%, #e8e9ea 55%, #f6f6f6 100%); box-shadow: 0 1px 4px rgba(0,0,0,.2); }
  .product-lens { position: absolute; left: 51px; top: 634px; width: 118px; height: 118px; border-radius: 50%; border: 5px solid var(--white); background: linear-gradient(180deg, #f6f8f4 0%, #f6f8f4 45%, #8f968e 46%, #b8bdb6 100%); box-shadow: 0 1px 6px rgba(0,0,0,.25); }
  .about { position: absolute; left: 363px; top: 656px; width: 272px; }
  .about h2 { font-weight: 400; font-size: 19px; line-height: 1.2; color: var(--ink); }
  .about p { font-size: 8.6px; line-height: 14.5px; color: var(--muted); margin-top: 7px; }
  .about p + p { margin-top: 0; }
  .btn-outline { position: relative; display: block; margin-top: 12px; width: 81px; height: 20px; border: 1px solid var(--blue); border-radius: 10px; font-size: 9.5px; line-height: 20px; color: var(--blue-dark); padding-left: 10px; }
  .btn-outline svg { position: absolute; right: 9px; top: 5px; }

  .testimonials { position: absolute; left: 0; top: 879px; width: 680px; height: 253px; background: linear-gradient(180deg, #e9eaec 0%, var(--band) 50%, #dfe0e2 100%); }
  .testimonials h2 { position: absolute; left: 0; top: 26px; width: 680px; text-align: center; font-weight: 400; font-size: 19px; line-height: 1.2; color: var(--ink); }
  .avatar { position: absolute; left: 298px; top: 60px; width: 84px; height: 84px; border-radius: 50%; border: 3px solid var(--white); background: linear-gradient(180deg, #c9b9a8 0%, #efe4da 60%, #f4f4f4 100%); box-shadow: 0 1px 4px rgba(0,0,0,.2); }
  .quote { position: absolute; left: 0; top: 163px; width: 680px; text-align: center; font-family: "Open Sans", Arial, sans-serif; font-size: 10px; line-height: 16.5px; color: #444; }
  .cite { position: absolute; right: 78px; top: 198px; font-family: "Open Sans", Arial, sans-serif; font-size: 10px; color: #444; }
  .cite small { font-size: 8.5px; }
  .dots { position: absolute; left: 319px; top: 224px; display: flex; gap: 2px; }
  .dots span { width: 8px; height: 8px; border-radius: 50%; background: #cfd0d2; border: 1px solid #b8b9bb; }
  .dots span.on { background: #7a7b7d; }

  .site-footer { position: absolute; left: 0; top: 1132px; width: 680px; height: 68px; background: var(--footer); color: var(--white); }
  .footer-links { position: absolute; left: 60px; top: 17px; font-size: 8.2px; font-family: Arial, sans-serif; }
  .copyright { position: absolute; left: 60px; top: 38px; font-size: 8.2px; font-family: Arial, sans-serif; }
  .social { position: absolute; left: 512px; top: 24px; display: flex; gap: 8px; }
  .social span { width: 21px; height: 21px; }
</style>
</head>
<body>

<header class="site-header">
  <div class="brand">Logo</div>
  <nav class="main-nav">
    <span>Home</span><span>About Us</span><span>Services</span><span>Testimonials</span><span>Contact</span>
  </nav>
</header>

<section class="hero" role="img" aria-label="Businessman in a dark suit behind hands holding a tablet showing an analytics dashboard">
  <h1 class="hero-title">Duis luctus tellus aliuam</h1>
  <p class="hero-text">Claritas est etiam processus dynamicus, qui sequi<br>tur mutationem consuetudium lectorum.</p>
  <div class="hero-btn">Read More</div>
</section>

<section class="feature" style="left:46px">
  <svg width="74" height="80" viewBox="0 0 74 80">
    <polygon points="37,2 71,21 71,59 37,78 3,59 3,21" fill="var(--blue)" stroke="var(--blue)" stroke-width="4" stroke-linejoin="round"/>
    <path d="M19 40 L55 25 L45 55 L36 45 Z" fill="#fff"/>
    <path d="M36 45 L55 25 L33 52 Z" fill="#cfe0f7"/>
  </svg>
  <h3>Services</h3>
  <p>Claritas est eteus dynamicuin thts,<br>qui sequitur mutatiem consuetud Claritas<br>dynamicusClaritas est etiam procss</p>
</section>

<section class="feature" style="left:240px">
  <svg width="74" height="80" viewBox="0 0 74 80">
    <polygon points="37,2 71,21 71,59 37,78 3,59 3,21" fill="var(--blue)" stroke="var(--blue)" stroke-width="4" stroke-linejoin="round"/>
    <circle cx="37" cy="40" r="17" fill="none" stroke="#fff" stroke-width="5" stroke-dasharray="5 3.9"/>
    <circle cx="37" cy="40" r="12" fill="#fff"/>
    <path d="M31 34 q4 2 3 6 q-3 2 -1 6 M40 31 q-1 4 4 5 q2 4 -2 8" fill="none" stroke="var(--blue)" stroke-width="2.2"/>
  </svg>
  <h3>Technologies</h3>
  <p>Claritas est eteus dynamicuin thts,<br>qui sequitur mutatiem consuetud Claritas<br>dynamicusClaritas est etiam procss</p>
</section>

<section class="feature" style="left:431px">
  <svg width="74" height="80" viewBox="0 0 74 80">
    <polygon points="37,2 71,21 71,59 37,78 3,59 3,21" fill="var(--blue)" stroke="var(--blue)" stroke-width="4" stroke-linejoin="round"/>
    <circle cx="37" cy="35" r="13" fill="none" stroke="#fff" stroke-width="3"/>
    <rect x="35.5" y="27" width="3" height="10" rx="1.5" fill="#fff"/>
    <circle cx="37" cy="41" r="1.8" fill="#fff"/>
    <rect x="31" y="50" width="12" height="2.5" rx="1" fill="#fff"/>
    <rect x="31" y="54.5" width="12" height="2.5" rx="1" fill="#fff"/>
    <rect x="33" y="59" width="8" height="2.5" rx="1" fill="#fff"/>
  </svg>
  <h3>Consulting</h3>
  <p>Claritas est eteus dynamicuin thts,<br>qui sequitur mutatiem consuetud Claritas<br>dynamicusClaritas est etiam procss</p>
</section>

<div class="divider"></div>

<div class="product-shot" role="img" aria-label="Website mockup of a business template with a city building banner and service icons"></div>
<div class="product-lens" role="img" aria-label="Magnified view of the mockup header and glass building facade"></div>

<section class="about">
  <h2>About Our Product</h2>
  <p>Claritas est etiam processus dynamicus, qui sequitur mutationem consuetud ium lectorum. Mirum est notare quam littera gothica, quam nunc putamus pa rum claram, anteposuerit litterarum formas humanitatis per.</p>
  <p>Duis autem vel eum iriure dolor in hendrerit in vulputate velit esse molestie c onsequat, vel illum dolore eu feugiat nulla facilisis at vero eros et accumsane t iusto odio dignissim qui blandit praesent luptatum zzril delenit.</p>
  <div class="btn-outline">Get Started
    <svg width="11" height="9" viewBox="0 0 11 9"><path d="M0 4.5 H9.5 M6 1 L9.5 4.5 L6 8" fill="none" stroke="var(--blue-dark)" stroke-width="1.4"/></svg>
  </div>
</section>

<section class="testimonials" role="img" aria-label="Faded grid of client portrait photos">
  <h2>Client Testimonials</h2>
  <div class="avatar" role="img" aria-label="Client portrait photo"></div>
  <p class="quote">I am so happy to have met you! Before Clear Voice Studio, I had vocal<br>problems that clouded my mind and made it zero fun to sing. Now I sing again and even have a weekly job as a speaker.</p>
  <p class="cite">- Marco, <small>Germany</small></p>
  <div class="dots"><span class="on"></span><span></span><span></span><span></span></div>
</section>

<footer class="site-footer">
  <p class="footer-links">Terms and Conditions | Privacy Promise | FAQ's | Contact Us</p>
  <p class="copyright">Copyright © 2013. All Rights Reserved.</p>
  <div class="social">
    <span style="background:var(--sq-1)"></span>
    <span style="background:var(--sq-2)"></span>
    <span style="background:var(--sq-3)"></span>
    <span style="background:var(--sq-4)"></span>
  </div>
</footer>

</body>
</html>
```